Stationary/business cards/letter head for IT Company
Vornel L.L.C.
Logo AI file uploaded.
Attention:
I've uploaded our current letter head with our old address. I would like to see stationary drafts with the top border (b/w picture) as seen in the PDF "letter head sample" uploaded. The picture taken is of the City of Phoenix Arizona at night.
Also, Please use black envelopes with a green flap.
Feel free to experiment.
RK/TPW/HN Team

```html
<!DOCTYPE html>
<html lang="en">
<head>
<meta charset="utf-8">
<title>Vornel L.L.C. Business Card</title>
<link href="https://fonts.googleapis.com/css2?family=Montserrat:wght@400;500;600;700&display=swap" rel="stylesheet">
<style>
  :root {
    --page-bg: #e9e9e7;
    --card-bg: #ffffff;
    --brand-green: #8cc63f;
    --band-grey: #9d9d9d;
    --text-dark: #5a5a5a;
    --text-soft: #9a9a9a;
  }
  * { margin: 0; padding: 0; box-sizing: border-box; }
  html, body {
    width: 1200px; height: 629px; overflow: hidden;
    background: var(--page-bg);
    font-family: "Montserrat", Arial, sans-serif;
  }
  .stage {
    position: relative; width: 1200px; height: 629px;
    display: flex; align-items: center; justify-content: center; gap: 60px;
  }
  .card {
    position: relative; width: 520px; height: 297px;
    background: var(--card-bg);
    box-shadow: 0 6px 18px rgba(0,0,0,0.12);
    overflow: hidden;
  }
  .brand-dot { display: block; border-radius: 50%; background: var(--brand-green); flex: none; }
  .brand-name { font-weight: 700; color: var(--brand-green); line-height: 1; }

  /* Card back */
  .card-back {
    display: flex; flex-direction: column; align-items: center; justify-content: center; gap: 16px;
  }
  .back-logo { display: flex; align-items: center; gap: 12px; }
  .back-logo .brand-dot { width: 34px; height: 34px; }
  .back-logo .brand-name { font-size: 30px; letter-spacing: 2px; }
  .tagline {
    font-size: 11px; letter-spacing: 2.5px; text-transform: uppercase; color: var(--text-soft);
  }

  /* Card front */
  .front-logo {
    position: absolute; top: 34px; left: 168px;
    display: flex; align-items: center; gap: 14px;
  }
  .front-logo .brand-dot { width: 46px; height: 46px; }
  .front-logo .brand-name { font-size: 44px; letter-spacing: 3px; }
  .brand-sub {
    position: absolute; top: 86px; left: 230px;
    font-size: 8px; letter-spacing: 2px; text-transform: uppercase; color: var(--text-soft);
  }
  .person { position: absolute; top: 128px; left: 34px; width: 230px; }
  .person-name {
    font-size: 12px; font-weight: 600; letter-spacing: 1.5px; text-transform: uppercase; color: var(--brand-green);
  }
  .person-title { font-size: 10px; color: var(--text-soft); margin-top: 4px; }
  .address {
    position: absolute; top: 190px; left: 34px;
    font-size: 10px; line-height: 15px; color: var(--text-dark);
  }
  .contact-list { position: absolute; top: 124px; left: 300px; list-style: none; }
  .contact-list li {
    display: flex; align-items: center; gap: 8px;
    font-size: 10px; color: var(--text-dark); height: 17px; white-space: nowrap;
  }
  .contact-icon { width: 11px; height: 11px; flex: none; }
  .contact-icon .icon-fill { fill: var(--brand-green); }
  .footer-rule {
    position: absolute; left: 0; right: 0; bottom: 42px; height: 1px; background: var(--brand-green);
  }
  .footer-band {
    position: absolute; left: 0; right: 0; bottom: 0; height: 34px;
    background: var(--band-grey);
    border-top: 3px solid var(--brand-green);
    display: flex; align-items: center; padding-left: 34px;
  }
  .web-address { font-size: 10px; letter-spacing: 2px; color: #ffffff; }
</style>
</head>
<body>
<main class="stage">
  <section class="card card-back">
    <div class="back-logo">
      <span class="brand-dot"></span>
      <span class="brand-name">VORNEL</span>
    </div>
    <p class="tagline">Building a smarter future</p>
  </section>

  <section class="card card-front">
    <div class="front-logo">
      <span class="brand-dot"></span>
      <span class="brand-name">VORNEL</span>
    </div>
    <p class="brand-sub">IT consulting company</p>

    <div class="person">
      <p class="person-name">Darin P. Maslow</p>
      <p class="person-title">Owner</p>
    </div>
    <p class="address">4410 N. Carrow Ave, Suite 12<br>Tempe, AZ 85281</p>

    <ul class="contact-list">
      <li>
        <svg class="contact-icon" viewBox="0 0 12 12"><path class="icon-fill" d="M2.5 1h2l1 3-1.3 1a7 7 0 0 0 2.8 2.8l1-1.3 3 1v2c0 .8-.7 1.5-1.5 1.5A9.5 9.5 0 0 1 1 2.5C1 1.7 1.7 1 2.5 1z"/></svg>
        602.555.0184
      </li>
      <li>
        <svg class="contact-icon" viewBox="0 0 12 12"><rect class="icon-fill" x="2" y="1" width="8" height="10" rx="1.5"/></svg>
        602.555.0237
      </li>
      <li>
        <svg class="contact-icon" viewBox="0 0 12 12"><rect class="icon-fill" x="1" y="4" width="10" height="6" rx="1"/><rect class="icon-fill" x="3" y="1" width="6" height="3"/></svg>
        602.555.0290
      </li>
      <li>
        <svg class="contact-icon" viewBox="0 0 12 12"><path class="icon-fill" d="M1 2.5h10v7H1z"/></svg>
        info@vornelllc.com
      </li>
      <li>
        <svg class="contact-icon" viewBox="0 0 12 12"><circle class="icon-fill" cx="6" cy="6" r="5"/></svg>
        vornelllc.com
      </li>
    </ul>

    <div class="footer-rule"></div>
    <div class="footer-band">
      <span class="web-address">www.vornelllc.com</span>
    </div>
  </section>
</main>
</body>
</html>
```